Internet of Things Word Template

We need a new MS word template for our high-tech, Internet of Things business that matches the enclosed template in terms of content (chapters and subsections), but that updates the style to match our new house style, that has a clear and simple style sheet, uses NUMBERED sections (style = 1.2.3.4.5), a clear TOC and that more closely matches our new website and some of the new documents enclosed. Website (www.varnoth-net.com) and house style guide www.varnoth-net.com/private/style-guide. We prefer a lighter style, needs to be professional and credible. Current template has become difficult to work with, so prefer someone starting from scratch. Cover design should be more Internet of Things related than just security-oriented, and can draw from graphics on our website.

Target Market(s)

Technical decision makers at companies that make Internet of Things devices or chip manufacturers who make the chips that go into many devices across industries like medical, automotive, smart buildings, smart cities, car dealerships, trucking, etc.

Font styles to use
Sans Serif

Colors
1763aa
ec1f27
f78f20

Requirements
Must have
• Close relationship to house style from website... but...
Lightly implemented. Not too heavy. Doesn't look too dark when printed in black and white.
Must be easy for the average person to customize for their needs. My colleagues are not Word experts.
Nice to have
• A nicely designed cover. That's the one place to really express our brand.
Should not have
• No over-use of icons or illustrations in the document itself.

```html
<!DOCTYPE html>
<html lang="en">
<head>
<meta charset="utf-8">
<title>Varnoth Net – Document Template Samples</title>
<link rel="stylesheet" href="https://fonts.googleapis.com/css2?family=Poppins:wght@300;400;500;600;700&display=swap">
<style>
  :root {
    --stage: #222b52;
    --paper: #ffffff;
    --ink: #262d58;
    --ink-deep: #0b1438;
    --brand-blue: #1763aa;
    --brand-red: #ec1f27;
    --brand-orange: #f78f20;
    --brand-grey: #5f6870;
    --muted: #b3b6c2;
    --tint-blue: #dfe9f4;
  }
  * { margin: 0; padding: 0; box-sizing: border-box; }
  html, body { width: 1200px; height: 1029px; overflow: hidden; }
  body {
    position: relative;
    background: var(--stage);
    font-family: "Poppins", sans-serif;
    color: var(--ink);
  }
  .panel-label {
    position: absolute;
    top: 141px;
    width: 460px;
    text-align: center;
    color: var(--paper);
    font-size: 16px;
    font-weight: 600;
    letter-spacing: 2.6px;
    line-height: 18px;
  }
  .panel-label--cover { left: 94px; }
  .panel-label--copyright { left: 645px; }

  .page { position: absolute; background: var(--paper); }
  .page--cover { left: 96px; top: 192px; width: 457px; height: 647px; }
  .page--copyright { left: 645px; top: 189px; width: 459px; height: 649px; }

  .pattern-area {
    position: absolute;
    width: 80px;
    height: 80px;
    background: linear-gradient(135deg, var(--tint-blue), #eef3f9);
  }

  .centered {
    position: absolute;
    left: 0; right: 0;
    text-align: center;
    line-height: 1;
  }

  .brand-name {
    position: absolute;
    color: var(--brand-grey);
    font-weight: 700;
    line-height: 1;
    letter-spacing: 0.3px;
  }
  .page--cover .brand-name { left: 0; right: 0; top: 24px; text-align: center; font-size: 24px; }
  .page--copyright .brand-name { left: 51px; top: 17px; font-size: 12.5px; color: #8e949b; }

  .cover-visual {
    position: absolute;
    left: 89px; top: 118px;
    width: 278px; height: 262px;
    border-radius: 50%;
    background: radial-gradient(circle at 50% 48%, #5fb3e0 0%, var(--brand-blue) 40%, #0e2a5c 75%, var(--ink-deep) 100%);
  }

  .cover-unit { top: 404px; font-size: 15px; font-weight: 500; }
  .cover-title { top: 438px; font-size: 27px; font-weight: 700; letter-spacing: 0.3px; }
  .cover-subject { top: 475px; font-size: 15.5px; font-weight: 600; }
  .cover-level { top: 515px; font-size: 12.5px; font-weight: 400; }
  .cover-date { top: 542px; font-size: 12px; font-weight: 400; }
  .cover-url { top: 627px; font-size: 11.5px; font-weight: 400; }

  .notice-title {
    position: absolute;
    left: 0; right: 0; top: 83px;
    text-align: center;
    font-size: 23px;
    font-weight: 600;
    line-height: 1;
  }
  .notice-body {
    position: absolute;
    left: 48px; top: 131px;
    width: 363px;
    font-size: 11px;
    line-height: 16.2px;
    text-align: justify;
    font-weight: 400;
  }
  .page-footer {
    position: absolute;
    right: 48px;
    text-align: right;
    color: var(--muted);
    font-weight: 300;
    line-height: 1;
  }
  .page-footer--level { top: 611px; font-size: 8.5px; }
  .page-footer--rights { top: 627px; font-size: 7.5px; }

  .status-note {
    position: absolute;
    left: 0; right: 0; top: 990px;
    text-align: center;
    color: var(--paper);
    font-size: 14px;
    font-weight: 400;
    line-height: 1;
  }
</style>
</head>
<body>
  <h2 class="panel-label panel-label--cover">SAMPLE COVER</h2>
  <h2 class="panel-label panel-label--copyright">SAMPLE COPYRIGHT PAGE</h2>

  <section class="page page--cover">
    <div class="pattern-area" style="left:369px;top:9px" role="img" aria-label="Decorative dot grid pattern"></div>

    <div class="brand-name">VARNOTH<br>NET</div>

    <div class="cover-visual" role="img" aria-label="Circular orbit emblem framing a photo of glowing light trails in a dim garage"></div>

    <p class="centered cover-unit">Varnoth Net Security</p>
    <h1 class="centered cover-title">TITLE HERE</h1>
    <p class="centered cover-subject">Subject</p>
    <p class="centered cover-level">Confidentiality level</p>
    <p class="centered cover-date">DD/MM/YYYY</p>
    <p class="centered cover-url">www.varnoth-net.com</p>

    <div class="pattern-area" style="left:9px;top:561px" role="img" aria-label="Decorative dot grid pattern"></div>
  </section>

  <section class="page page--copyright">
    <div class="brand-name">VARNOTH<br>NET</div>
    <h1 class="notice-title">COPYRIGHT NOTICE</h1>
    <p class="notice-body">Varnoth Net Security, a business unit of Corvane SA is a member of the Varnoth Group of Companies. This document is the intellectual property of Varnoth Net Security and contains confidential and privileged information. The reproduction, modification, or communication to third parties (or to other than the addressee) of any part of this document is strictly prohibited without the prior written consent from Corvane SA.</p>
    <p class="page-footer page-footer--level">CONFIDENTIALITY LEVEL 2</p>
    <p class="page-footer page-footer--rights">© 2020 Corvane SA / All rights reserved</p>

    <div class="pattern-area" style="left:9px;top:564px" role="img" aria-label="Decorative dot grid pattern"></div>
  </section>

  <p class="status-note">*Still working on full design</p>
</body>
</html>
```